Redesign and move to Wordpress for qorvanta.com

Our website needs a redesign and at the same time we are moving it to Wordpress. Please help us with a new digital professional look and feel.

We are an Australian Software Engineering company specialising in advanced software development using in A.I., PLatform Engineering, Integration and Cloud. See the current qorvanta.com for more information about us.

```html
<!DOCTYPE html>
<html lang="en">
<head>
<meta charset="utf-8">
<title>qorvanta – Reliable Smart Software Engineering</title>
<link href="https://fonts.googleapis.com/css2?family=Saira:wght@300;400;500&family=Poppins:wght@300;400;500&display=swap" rel="stylesheet">
<style>
:root{
  --bg:#020a22;
  --bg-deep:#010617;
  --card:#041233;
  --card-line:#0e2552;
  --teal:#2fd9c8;
  --cyan:#19c3ee;
  --blue:#2b8cff;
  --text:#ffffff;
  --muted:#c9d3e6;
  --tile:#0a2a66;
}
*{margin:0;padding:0;box-sizing:border-box}
html,body{width:1200px;height:2936px;overflow:hidden;background:var(--bg)}
body{font-family:"Poppins",sans-serif;color:var(--text);position:relative}
.page{position:relative;width:1200px;height:2936px;overflow:hidden;
  background:radial-gradient(ellipse 600px 500px at 600px 150px,#0c2a6b 0%,rgba(2,10,34,0) 70%),
  radial-gradient(ellipse 700px 260px at 600px 2936px,#0a5a6a 0%,rgba(2,10,34,0) 75%),var(--bg)}
.abs{position:absolute}
.heading{font-family:"Saira",sans-serif;font-weight:400}
.brand{display:flex;align-items:center;gap:12px;font-family:"Saira",sans-serif;font-weight:400;font-size:27px;letter-spacing:1px}
.brand-mark{width:30px;height:30px;border:3px solid #fff}
.nav a{position:absolute;top:28px;font-size:12px;color:#fff;text-decoration:none;white-space:nowrap}
.nav a.active{color:var(--cyan)}
.btn{display:flex;align-items:center;justify-content:space-between;font-size:12.5px;text-decoration:none;color:#fff;white-space:nowrap}
.btn .sq{width:10px;height:10px;background:var(--bg-deep);flex:none}
.btn-solid{background:var(--teal);color:#0a2540;padding:0 18px}
.btn-outline{border:1.5px solid var(--teal);padding:0 12px;color:#fff}
.btn-outline .sq{background:none;border:1.5px solid #fff;width:9px;height:9px}
.section-title{font-family:"Saira",sans-serif;font-weight:400;font-size:32px;text-align:center;width:1200px;left:0}
.insight{background:var(--card);border:1px solid var(--card-line);text-align:center;padding:30px 18px}
.insight h3{font-family:"Saira",sans-serif;font-weight:400;font-size:18px}
.insight .sub{color:var(--blue);font-size:11px;line-height:13px;margin-top:4px}
.insight p{font-size:10.5px;line-height:15px;margin:16px auto 0;width:240px;color:#e5eaf4}
.insight .photo{position:absolute;left:19px;right:19px;top:172px;height:161px}
.circle-arrow{width:15px;height:15px;border-radius:50%;background:var(--teal)}
.tile{background:linear-gradient(160deg,#0b2a66,#061540 60%,#04102f);display:flex;align-items:center;justify-content:center;font-family:"Poppins",sans-serif;font-weight:500;font-size:19px;color:#fff;white-space:nowrap}
.tile.small{font-size:14px}
.service{background:var(--card);border:1px solid var(--card-line);text-align:center}
.service .icon{width:66px;height:66px;border-radius:50%;background:#0b2a5a;margin:30px auto 0;display:flex;align-items:center;justify-content:center}
.service h3{font-family:"Saira",sans-serif;font-weight:400;font-size:17px;margin-top:18px;line-height:20px}
.service p{font-size:10.5px;line-height:15px;color:#d8deea;width:230px;margin:10px auto 0}
.service .go{margin-top:12px;color:var(--teal);font-size:16px}
.service.featured{background:linear-gradient(180deg,#062a4e,#0b4e62)}
.service.featured .icon{background:var(--teal)}
.service .corner{position:absolute;right:-1px;bottom:-1px;width:14px;height:14px;border:1px solid var(--card-line);background:var(--bg)}
.service.featured .corner{background:var(--teal);border-color:var(--teal)}
.stat{border:16px solid var(--tile)}
.stat.teal{border-color:#56c9bf}
.stat-inner{width:100%;height:100%;display:flex;flex-direction:column;align-items:center;justify-content:center;text-align:center}
.about p{font-size:10.5px;line-height:15.6px;color:#dfe5f1;margin-bottom:14px}
.field{border:1px solid #2b63b8;background:transparent;color:#9fb0cc;font-size:11.5px;padding:0 11px;display:flex;align-items:center}
.footer h4{font-family:"Saira",sans-serif;font-weight:400;font-size:17px}
.footer .item{display:flex;align-items:center;gap:8px;font-size:9.5px;position:absolute;white-space:nowrap}
.footer .dot{width:16px;height:16px;border:1px solid #fff;border-radius:50%;display:flex;align-items:center;justify-content:center}
.footer .link{position:absolute;font-size:9.5px}
</style>
</head>
<body>
<div class="page">

<header>
  <div class="abs brand" style="left:112px;top:18px"><span class="brand-mark"></span>qorvanta</div>
  <nav class="nav">
    <a class="active" style="left:471px">Home</a>
    <a style="left:539px">About Us</a>
    <a style="left:625px">Services <span style="color:var(--cyan)">⌄</span></a>
    <a style="left:707px">Blog</a>
  </nav>
  <svg class="abs" style="left:949px;top:31px" width="11" height="11" viewBox="0 0 11 11"><circle cx="4.5" cy="4.5" r="3.5" fill="none" stroke="#fff" stroke-width="1.4"/><line x1="7.2" y1="7.2" x2="10" y2="10" stroke="#fff" stroke-width="1.4"/></svg>
  <a class="abs btn btn-outline" style="left:982px;top:19px;width:104px;height:34px;font-size:11.5px;border-color:#2b63b8">Contact Us <span class="sq"></span></a>
</header>

<section>
  <div class="abs" style="left:0;width:1200px;top:117px;text-align:center;color:var(--cyan);font-size:16px;font-weight:500">Welcome to qorvanta</div>
  <h1 class="abs heading" style="left:0;width:1200px;top:136px;text-align:center;font-size:45px;font-weight:400;letter-spacing:.5px">Reliable Smart Software Engineering</h1>
  <div class="abs" role="img" aria-label="Glowing cyan emblem standing on a lit circular platform"
       style="left:182px;top:205px;width:838px;height:330px;background:radial-gradient(ellipse 260px 150px at 50% 50%,#1d5bb8 0%,#0b2a6b 45%,rgba(2,10,34,0) 80%)"></div>
</section>

<section>
  <h2 class="abs section-title" style="top:585px">Insights</h2>
  <div class="abs circle-arrow" style="left:78px;top:829px"></div>
  <div class="abs circle-arrow" style="left:1109px;top:829px"></div>

  <article class="abs insight" style="left:113px;top:646px;width:317px;height:354px">
    <h3>Ai in Software Engineering</h3>
    <div class="sub">10 unexpected ways to use<br>Codeharbor Pilot</div>
    <p>(Codeharbor Blog) Codeharbor Pilot is widely known for its code generation feature. Learn how the AI assistant's abilities can extend beyond just code generation.</p>
    <div class="photo" role="img" aria-label="Photo of white server boxes linked by black cables" style="background:linear-gradient(135deg,#e8e8e8,#9a9a9a 60%,#d0d0d0)"></div>
  </article>
  <article class="abs insight" style="left:448px;top:646px;width:306px;height:354px">
    <h3>Industry Research</h3>
    <div class="sub">SPARO: A general-purpose framework<br>for prompt optimization</div>
    <p>(Velmora Labs) Large language models (LLMs) have revolutionized various tasks, but prompt engineering remains a challenge.</p>
    <div class="photo" role="img" aria-label="Illustration of a glowing digital data display in gold and blue" style="background:linear-gradient(135deg,#1a3260,#6a5a3a 55%,#d6b476)"></div>
  </article>
  <article class="abs insight" style="left:783px;top:646px;width:305px;height:354px">
    <h3>Business Insights</h3>
    <div class="sub">How Storytelling Helps Data-driven<br>Teams Succeed</div>
    <p>(Eastbridge School of Management) Winning leaders know that data alone isn't enough. It's the art of storytelling that drives sustained performance.</p>
    <div class="photo" role="img" aria-label="Photo of a business team meeting around a table with a laptop" style="background:linear-gradient(135deg,#d8dde4,#7b6a5e 55%,#3a3a40)"></div>
  </article>

  <a class="abs btn btn-solid" style="left:501px;top:1023px;width:198px;height:37px">View All News &amp; Articles <span class="sq"></span></a>
</section>

<section>
  <h2 class="abs heading" style="left:113px;width:360px;top:1106px;text-align:center;font-size:30px">Our Partners</h2>
  <h2 class="abs heading" style="left:713px;width:373px;top:1108px;text-align:center;font-size:30px">Our Customers</h2>

  <div class="abs tile" style="left:113px;top:1168px;width:178px;height:80px">Tunevale</div>
  <div class="abs tile" style="left:304px;top:1168px;width:178px;height:112px">Velmora</div>
  <div class="abs tile" style="left:113px;top:1262px;width:178px;height:111px">Codeharbor</div>
  <div class="abs tile" style="left:304px;top:1292px;width:178px;height:81px;font-size:24px">Rivlet</div>

  <div class="abs" style="left:540px;top:1216px;width:118px;height:118px;border:5px solid #1f6fb8"></div>

  <div class="abs tile small" style="left:713px;top:1170px;width:117px;height:96px">Harbourline</div>
  <div class="abs tile" style="left:841px;top:1170px;width:116px;height:96px;font-size:17px">Brightfund</div>
  <div class="abs tile" style="left:970px;top:1170px;width:116px;height:96px">QBX</div>
  <div class="abs tile" style="left:713px;top:1279px;width:117px;height:95px">SVQ</div>
  <div class="abs tile" style="left:841px;top:1279px;width:116px;height:95px">MRZ</div>
  <div class="abs tile" style="left:970px;top:1279px;width:116px;height:95px;font-size:8px;letter-spacing:.5px">VALLEY LANE GROUP</div>
</section>

<section>
  <h2 class="abs section-title" style="top:1420px">Our Services</h2>

  <article class="abs service" style="left:111px;top:1485px;width:306px;height:248px">
    <div class="icon"><svg width="38" height="38" viewBox="0 0 38 38" fill="none" stroke="#9fd8ff" stroke-width="1.5"><circle cx="14" cy="14" r="6"/><circle cx="14" cy="14" r="10" stroke-dasharray="4 3"/><circle cx="26" cy="26" r="5"/><circle cx="26" cy="26" r="8" stroke-dasharray="3 3"/></svg></div>
    <h3>Enterprise Systems Integration</h3>
    <p>Automate your business processes internally or externally to improve data quality and process efficiency.</p>
    <div class="go">→</div>
    <span class="corner"></span>
  </article>
  <article class="abs service" style="left:444px;top:1485px;width:307px;height:248px">
    <div class="icon"><svg width="38" height="38" viewBox="0 0 38 38" fill="none" stroke="#9fd8ff" stroke-width="1.5"><ellipse cx="16" cy="9" rx="9" ry="4"/><path d="M7 9v16c0 2 4 4 9 4M25 9v8M7 17c0 2 4 4 9 4"/><circle cx="27" cy="27" r="6" fill="#2fd9c8" stroke="#2fd9c8"/></svg></div>
    <h3>Real-time Data Analytics</h3>
    <p>Being able to react to changing business conditions in a precise intelligent way is becoming increasingly important.</p>
    <div class="go">→</div>
    <span class="corner"></span>
  </article>
  <article class="abs service featured" style="left:778px;top:1485px;width:308px;height:248px">
    <div class="icon"><svg width="38" height="38" viewBox="0 0 38 38" fill="none" stroke="#063040" stroke-width="1.6"><circle cx="19" cy="19" r="6"/><circle cx="19" cy="19" r="11" stroke-dasharray="5 3"/><circle cx="19" cy="4" r="2"/><circle cx="19" cy="34" r="2"/><circle cx="4" cy="19" r="2"/><circle cx="34" cy="19" r="2"/></svg></div>
    <h3>Custom Development of<br>Intelligent Business Applications</h3>
    <p>Our expertise in platform engineering, iPaaS, building distributed systems &amp; enterprise systems integration.</p>
    <div class="go" style="color:#fff">→</div>
    <span class="corner"></span>
  </article>

  <a class="abs btn btn-solid" style="left:522px;top:1767px;width:155px;height:37px">View All Services <span class="sq"></span></a>
</section>

<section>
  <div class="abs stat" style="left:113px;top:1868px;width:192px;height:114px">
    <div class="stat-inner" style="background:#031033">
      <div style="font-size:12.5px">Company size:</div>
      <div class="heading" style="font-size:44px;line-height:44px">500+</div>
    </div>
  </div>
  <div class="abs stat teal" style="left:113px;top:2009px;width:192px;height:221px">
    <div class="stat-inner" role="img" aria-label="Photo of engineers working at computers" style="background:linear-gradient(180deg,#5a6a78,#2a3340 55%,#0c1830);justify-content:flex-end;padding-bottom:18px">
      <div class="heading" style="font-size:36px;line-height:36px">2013</div>
      <div style="font-size:12.5px">Founded year</div>
    </div>
  </div>
  <div class="abs stat" style="left:336px;top:1868px;width:192px;height:221px">
    <div class="stat-inner" role="img" aria-label="Illustration of a glowing medical cross held in a hand" style="background:radial-gradient(circle at 50% 40%,#5fd2ff,#1a6fb0 45%,#0b2a5a);justify-content:flex-end;padding-bottom:12px">
      <div style="font-size:14.5px;line-height:19px">Health &amp; Finance<br>Enterprise</div>
    </div>
  </div>
  <div class="abs stat teal" style="left:336px;top:2116px;width:192px;height:114px">
    <div class="stat-inner" role="img" aria-label="Image of a hand touching a digital interface" style="background:linear-gradient(135deg,#1a3fa0,#3a6fd0 60%,#6aa0e0)">
      <div style="font-size:14.5px">Tech Geography</div>
    </div>
  </div>

  <div class="abs about" style="left:689px;top:1868px;width:378px">
    <h2 class="heading" style="font-size:30px;margin-bottom:12px">About Us qorvanta</h2>
    <p>Since our inception in 2013, we have been on a mission to make complex custom enterprise integration accessible to any organization, regardless of industry, size, or location.</p>
    <p>Our journey began with a focus on Integration Architecture, quickly moving into delivering bespoke systems integration using Velmora technologies like Conduxa, Loomnet, Quarrydb, and Serviq. Our commitment to excellence quickly earned us recognition, &amp; in 2014, we became a proud Velmora Gold Partner, achieving this accolade with the creation of our first 100% native Skyvane cloud solution. We have upheld this esteemed partnership ever since.</p>
    <p>By 2017, we had implemented one of the first large-scale Velmora Skyvane iPaaS solutions in Australia, pioneering the use of new Skyvane integration products in conjunction with the Velmora Product Team.</p>
  </div>
  <a class="abs btn btn-outline" style="left:689px;top:2169px;width:115px;height:34px;border-color:#2b63b8">Read More <span class="sq"></span></a>
</section>

<section>
  <h2 class="abs section-title" style="top:2285px;font-size:31px">Tomorrow, Delivered Today</h2>
  <div class="abs field" style="left:315px;top:2348px;width:278px;height:34px">First Name*</div>
  <div class="abs field" style="left:604px;top:2348px;width:278px;height:34px">Last Name*</div>
  <div class="abs field" style="left:315px;top:2394px;width:278px;height:34px">Email*</div>
  <div class="abs field" style="left:604px;top:2394px;width:278px;height:34px">Mobile Phone Number*</div>
  <div class="abs field" style="left:315px;top:2441px;width:567px;height:63px;align-items:flex-start;padding-top:10px">Message</div>
  <a class="abs btn btn-solid" style="left:531px;top:2516px;width:136px;height:37px;font-size:11.5px">Submit <span class="sq"></span></a>
</section>

<footer class="footer">
  <div class="abs brand" style="left:112px;top:2596px;font-size:28px"><span class="brand-mark" style="width:34px;height:34px"></span>qorvanta</div>
  <div class="abs" style="left:112px;top:2656px;width:250px;font-size:9.5px;line-height:14.5px">We have been on a mission to make complex custom enterprise integration accessible to any organisation, regardless of industry, size, or location</div>
  <div class="abs" style="left:112px;top:2709px;font-size:9.5px">© 2025 All Rights Reserved By qorvanta</div>

  <h4 class="abs" style="left:427px;top:2596px">Contact Us</h4>
  <div class="item" style="left:427px;top:2631px"><span class="dot"><svg width="8" height="10" viewBox="0 0 8 10"><path d="M4 10C1 6 0 5 0 4a4 4 0 0 1 8 0c0 1-1 2-4 6z" fill="#fff"/></svg></span>Suite 402, 18 Harbour Lane Melbourne, VIC, 3006</div>
  <div class="item" style="left:427px;top:2656px"><span class="dot"><svg width="9" height="9" viewBox="0 0 9 9"><path d="M1 1l2-1 1 2-1 1c1 2 2 3 3 3l1-1 2 1-1 2C4 8 1 5 1 1z" fill="#fff"/></svg></span>1800 555 019</div>
  <div class="item" style="left:427px;top:2682px;color:var(--teal)"><span class="dot"><svg width="9" height="7" viewBox="0 0 9 7"><rect width="9" height="7" fill="#fff"/><path d="M0 0l4.5 4L9 0" stroke="#020a22" fill="none"/></svg></span>info@qorvanta.com</div>

  <h4 class="abs" style="left:751px;top:2596px">Quick Links</h4>
  <span class="link" style="left:752px;top:2629px">Home</span>
  <span class="link" style="left:752px;top:2649px">About</span>
  <span class="link" style="left:752px;top:2669px">Services</span>
  <span class="link" style="left:752px;top:2689px">Blog</span>
  <span class="link" style="left:752px;top:2709px">Contact Us</span>

  <h4 class="abs" style="left:933px;top:2596px">Follow Us</h4>
  <div class="item" style="left:933px;top:2631px"><span class="dot"></span>Friendsphere</div>
  <div class="item" style="left:933px;top:2656px"><span class="dot"></span>Netlinkr</div>
  <div class="item" style="left:933px;top:2682px"><span class="dot"></span>Chatterlane</div>

  <div class="abs heading" aria-hidden="true" style="left:0;width:1200px;top:2730px;text-align:center;font-size:130px;font-weight:300;letter-spacing:8px;color:rgba(40,90,140,.22)">qorvanta</div>
</footer>

</div>
</body>
</html>
```